Law firm business card

Information:

Me Marisa Delacourt

website: velmont-juris.ca
email: marisa@velmont-juris.ca
Phone: 514 372-5106
Fax: 514 372-5107

Address:
Delacourt and associates
2917 Brisebois
Montreal, QC
H3K 2T9

Areas of Expertise:
Franchise Agreements, Financing, Acquisition, Real Estate Development, Commercial Agreements and Corporate Law

Target Market(s)

executives, companie managers

Industry/Entity Type

Business

Colors
f78f20
000000

Requirements
Must have
• Must use the logo, the logo is available here:

https://www.filevault-share.net/sh/qe82kd0pl1m7/BXtr9LmQw3zPaYkN

```html
<!DOCTYPE html>
<html lang="en">
<head>
<meta charset="utf-8">
<title>Delacourt and associates — Business Card</title>
<link rel="stylesheet" href="https://fonts.googleapis.com/css2?family=Arimo:wght@400&display=swap">
<style>
  :root {
    --page: #ffffff;
    --card: #231f20;
    --card-edge: #5a5a5a;
    --accent: #fcc72e;
    --ink: #ffffff;
  }
  * { box-sizing: border-box; margin: 0; padding: 0; }
  html, body {
    width: 1200px;
    height: 698px;
    overflow: hidden;
    background: var(--page);
  }
  .canvas {
    position: relative;
    width: 1200px;
    height: 698px;
    font-family: "Arimo", Arial, sans-serif;
    color: var(--ink);
  }
  .card {
    position: absolute;
    width: 680px;
    height: 402px;
    background: var(--card);
    border: 2px solid var(--card-edge);
    overflow: hidden;
  }
  .card--back { left: 0; top: 0; }
  .card--front { left: 520px; top: 296px; }
  .corner {
    position: absolute;
    display: block;
  }
  .corner--top-left { left: 0; top: 0; width: 200px; height: 156px; }
  .corner--bottom-right { right: 0; bottom: 0; width: 198px; height: 152px; }
  .contact-list {
    position: absolute;
    left: 34px;
    top: 219px;
    display: grid;
    grid-template-columns: 114px auto;
    font-size: 28px;
    line-height: 35.6px;
    white-space: nowrap;
  }
  .card-name {
    position: absolute;
    left: 0;
    width: 650px;
    top: 143px;
    text-align: center;
    font-size: 37px;
    line-height: 44px;
    white-space: nowrap;
  }
  .card-address {
    position: absolute;
    left: 14px;
    top: 311px;
    font-size: 24px;
    line-height: 31px;
    font-style: normal;
    white-space: pre;
  }
</style>
</head>
<body>
<main class="canvas">
  <section class="card card--back">
    <svg class="corner corner--top-left" viewBox="0 0 200 156" role="img" aria-label="Decorative yellow tiled pattern corner">
      <polygon points="0,0 200,0 0,156" fill="var(--accent)"/>
    </svg>
    <dl class="contact-list">
      <dt>Website</dt><dd>: velmont-juris.ca</dd>
      <dt>Email</dt><dd>: marisa@velmont-juris.ca</dd>
      <dt>Phone</dt><dd>: 514 372-5106</dd>
      <dt>Fax</dt><dd>: 514 372-5107</dd>
    </dl>
  </section>

  <section class="card card--front">
    <h1 class="card-name" style="font-weight:400">Me Marisa Delacourt</h1>
    <address class="card-address">Address: Delacourt and associates
2917 Brisebois  Montreal, QC, H3K 2T9</address>
    <svg class="corner corner--bottom-right" viewBox="0 0 198 152" role="img" aria-label="Decorative yellow tiled pattern corner">
      <polygon points="198,0 198,152 0,152" fill="var(--accent)"/>
    </svg>
  </section>
</main>
</body>
</html>
```